Valentine's Day menu

Our establishment on Brasserie Orville, (bar - brasserie - wine bar); Offers a menu for Valentine's Day, one that will be on site and another in delivery.

Menu on site:

Starter: Oysters, warm champagne flambé

Dish: Grilled tournedos, braised endives and Jerusalem artichokes
Ranger Sauce
Sole meunière, lemon sauce, steamed potatoes, rice

Dessert: Tiramisu with red fruits - Flambéed Crêpe Suzette

Menu at 29.90€

Delivery menu: Raclette platter with Savoy cheeses - Pierrade platter and fresh vegetables.
Half-bottle of VALDORIEUX BLANCS DE BLANS.

Please use the Valentine's Day theme, use our logo and colors (attached). The goal is to get as many reservations as possible.

Reservation required at: 06 38 72 15 09
Brasserie Orville
18 rue Fernand Gaudry 62870 VALMONT

I remain at your disposal.

- Rate ; 45€ / Person

```html
<!DOCTYPE html>
<html lang="en">
<head>
<meta charset="utf-8">
<title>Brasserie Orville – Valentine's Day Menus</title>
<link href="https://fonts.googleapis.com/css2?family=Montserrat:wght@400;500;600;700&family=Playfair+Display:wght@700;900&display=swap" rel="stylesheet">
<style>
  :root {
    --page-bg: #dedede;
    --paper: #f3efe5;
    --gold: #d1a133;
    --gold-light: #f2d37a;
    --gold-deep: #a9781a;
    --ink: #111111;
    --shadow: #1c1c1c;
  }
  * { box-sizing: border-box; margin: 0; padding: 0; }
  html, body { width: 693px; height: 1200px; overflow: hidden; }
  body {
    background: var(--page-bg);
    font-family: 'Montserrat', sans-serif;
    color: var(--ink);
    position: relative;
  }
  .menu-card {
    position: absolute;
    left: 127px;
    width: 440px;
    height: 570px;
    background: var(--paper);
    box-shadow: -4px 4px 0 var(--shadow);
    overflow: hidden;
  }
  .menu-card--delivery { top: 20px; }
  .menu-card--onsite { top: 610px; }

  .frame {
    position: absolute;
    left: 20px; right: 20px; top: 19px; bottom: 22px;
    border: 1px solid var(--gold);
  }
  .heart-cluster {
    position: absolute;
    border-radius: 50%;
    background: radial-gradient(ellipse at center, rgba(232,190,80,0.75) 0%, rgba(216,172,62,0.35) 55%, rgba(243,239,229,0) 75%);
  }
  .heart-cluster--top-left { left: 22px; top: 30px; width: 90px; height: 140px; }
  .heart-cluster--top-right { right: 22px; top: 30px; width: 90px; height: 140px; }
  .heart-cluster--bottom { left: 105px; bottom: -18px; width: 230px; height: 80px; }

  .brand-name {
    position: absolute; top: 62px; left: 0; right: 0;
    font-family: 'Montserrat', sans-serif;
    font-weight: 500;
    font-size: 13px;
    line-height: 16px;
    letter-spacing: 1px;
    color: var(--gold);
    text-align: center;
  }

  .headline {
    position: absolute; top: 100px; left: 0; right: 0;
    text-align: center;
    font-family: 'Playfair Display', serif;
    font-weight: 700;
    font-size: 31px;
    color: var(--gold);
  }
  .menu-band {
    position: absolute; top: 148px; left: 145px;
    width: 150px; height: 23px;
    background: linear-gradient(90deg, var(--gold-deep), var(--gold-light) 45%, var(--gold) 75%, var(--gold-deep));
    clip-path: polygon(0 0, 100% 0, 93% 50%, 100% 100%, 0 100%, 7% 50%);
    text-align: center;
    font-family: 'Playfair Display', serif;
    font-weight: 700;
    font-size: 19px;
    line-height: 23px;
    color: var(--ink);
  }

  .flourish {
    position: absolute;
    background: linear-gradient(90deg, rgba(209,161,51,0), rgba(209,161,51,0.6) 30%, rgba(242,211,122,0.9) 50%, rgba(209,161,51,0.6) 70%, rgba(209,161,51,0));
    border-radius: 50%;
  }
  .rule {
    position: absolute; height: 2px;
    background: linear-gradient(90deg, var(--gold), var(--gold-light) 50%, var(--gold-deep));
  }

  .delivery-title {
    position: absolute; top: 240px; left: 0; right: 0;
    text-align: center;
    font-family: 'Playfair Display', serif;
    font-weight: 900;
    font-size: 24px;
    line-height: 28px;
  }
  .item {
    position: absolute; left: 0; right: 0;
    text-align: center;
    font-size: 11px;
    font-weight: 500;
  }
  .dots {
    position: absolute; height: 0;
    border-top: 1px dotted var(--gold);
  }
  .dots--grey { border-top-color: #8c8478; }

  .price-label {
    position: absolute; left: 0; right: 0;
    text-align: center;
    font-family: 'Playfair Display', serif;
    font-weight: 700;
    color: var(--ink);
  }
  .price-row {
    position: absolute; left: 0; right: 0;
    display: flex; justify-content: center; align-items: center; gap: 6px;
  }
  .price-box {
    background: var(--gold);
    color: var(--ink);
    height: 25px;
    padding: 0 5px;
    line-height: 25px;
  }
  .price-box--rate { font-weight: 700; font-size: 15px; }
  .price-box--set { font-family: 'Playfair Display', serif; font-weight: 700; font-size: 21px; padding: 0 10px; }

  .contact {
    position: absolute; top: 470px; left: 0; right: 0;
    display: flex; justify-content: center; align-items: flex-start; gap: 14px;
    font-size: 9.5px; font-weight: 600; line-height: 12px;
  }
  .contact-item { display: flex; gap: 4px; align-items: flex-start; }
  .contact-divider { width: 1px; height: 18px; background: var(--ink); margin-top: 2px; }

  .course-head {
    position: absolute; left: 0; right: 0; height: 30px;
  }
  .course-head .flourish { left: 175px; top: 0; width: 90px; height: 12px; }
  .course-head .rule { left: 147px; width: 146px; }
  .course-head .rule--top { top: 14px; }
  .course-head .rule--bottom { top: 30px; }
  .course-name {
    position: absolute; top: 15px; left: 0; right: 0;
    text-align: center; font-size: 12px; font-weight: 500;
    letter-spacing: 3px; line-height: 15px;
  }
  .course-heart { position: absolute; top: 14px; width: 20px; height: 18px; }
  .course-heart--left { left: 116px; }
  .course-heart--right { right: 116px; }
  .course-desc {
    position: absolute; left: 0; right: 0;
    text-align: center; font-size: 9.5px; line-height: 12px; font-weight: 400;
  }
</style>
</head>
<body>

<!-- Delivery menu -->
<section class="menu-card menu-card--delivery" aria-label="Valentine's Day delivery menu">
  <div class="frame"></div>
  <div class="heart-cluster heart-cluster--top-left" role="img" aria-label="Golden hearts decoration"></div>
  <div class="heart-cluster heart-cluster--top-right" role="img" aria-label="Golden hearts decoration"></div>
  <div class="heart-cluster heart-cluster--bottom" role="img" aria-label="Pile of golden hearts"></div>

  <p class="brand-name">BRASSERIE ORVILLE</p>
  <h1 class="headline">Valentine's Day</h1>
  <div class="menu-band">MENU</div>

  <div class="flourish" style="left:127px; top:198px; width:186px; height:30px;" role="img" aria-label="Gold baroque flourish ornament"></div>
  <div class="rule" style="left:75px; top:234px; width:290px;"></div>
  <h2 class="delivery-title">DELIVERY MENU:</h2>
  <div class="rule" style="left:75px; top:270px; width:290px;"></div>

  <p class="item" style="top:297px;">Raclette platter with Savoy cheeses</p>
  <div class="dots" style="left:103px; top:324px; width:234px;"></div>
  <p class="item" style="top:341px;">Pierrade platter and fresh vegetables.</p>
  <div class="dots" style="left:103px; top:366px; width:234px;"></div>
  <p class="item" style="top:385px;">Half-bottle of VALDORIEUX BLANCS DE BLANS.</p>

  <p class="price-label" style="top:406px; font-size:15px;">RATE</p>
  <div class="price-row" style="top:425px;">
    <svg width="30" height="22" viewBox="0 0 30 22"><polygon points="0,0 30,0 30,22 0,22 9,11" fill="#111"/></svg>
    <div class="price-box price-box--rate">45€ / PERSON</div>
    <svg width="30" height="22" viewBox="0 0 30 22"><polygon points="0,0 30,0 21,11 30,22 0,22" fill="#111"/></svg>
  </div>

  <div class="contact">
    <div class="contact-item">
      <svg width="11" height="11" viewBox="0 0 24 24"><path d="M6.6 10.8a15 15 0 0 0 6.6 6.6l2.2-2.2a1 1 0 0 1 1-.25 11.4 11.4 0 0 0 3.6.57 1 1 0 0 1 1 1V20a1 1 0 0 1-1 1A17 17 0 0 1 3 4a1 1 0 0 1 1-1h3.5a1 1 0 0 1 1 1c0 1.250.2 2.450.57 3.570a1 1 0 0 1-.25 1z" fill="none" stroke="#111" stroke-width="2"/></svg>
      <span>Reservation required at:<br>06 38 72 15 09</span>
    </div>
    <div class="contact-divider"></div>
    <div class="contact-item">
      <svg width="11" height="12" viewBox="0 0 24 26"><path d="M12 2a7 7 0 0 0-7 7c0 5 7 12 7 12s7-7 7-12a7 7 0 0 0-7-7z" fill="none" stroke="#111" stroke-width="2"/><circle cx="12" cy="9" r="2.5" fill="none" stroke="#111" stroke-width="2"/><path d="M4 24h16" stroke="#111" stroke-width="2"/></svg>
      <span>18 rue Fernand<br>Gaudry 62870 VALMONT</span>
    </div>
  </div>
</section>

<!-- On-site menu -->
<section class="menu-card menu-card--onsite" aria-label="Valentine's Day on-site menu">
  <div class="frame"></div>
  <div class="heart-cluster heart-cluster--top-left" role="img" aria-label="Golden hearts decoration"></div>
  <div class="heart-cluster heart-cluster--top-right" role="img" aria-label="Golden hearts decoration"></div>
  <div class="heart-cluster heart-cluster--bottom" role="img" aria-label="Pile of golden hearts"></div>

  <p class="brand-name">BRASSERIE ORVILLE</p>
  <h1 class="headline">Valentine's Day</h1>
  <div class="menu-band">MENU</div>

  <div class="course-head" style="top:190px;">
    <div class="flourish" role="img" aria-label="Small gold flourish ornament"></div>
    <div class="rule rule--top"></div>
    <svg class="course-heart course-heart--left" viewBox="0 0 24 22"><path d="M12 21s-10-6-10-13a5 5 0 0 1 10-2 5 5 0 0 1 10 2c0 7-10 13-10 13z" fill="#111"/></svg>
    <p class="course-name">STARTER</p>
    <svg class="course-heart course-heart--right" viewBox="0 0 24 22"><path d="M12 21s-10-6-10-13a5 5 0 0 1 10-2 5 5 0 0 1 10 2c0 7-10 13-10 13z" fill="#111"/></svg>
    <div class="rule rule--bottom"></div>
  </div>
  <p class="course-desc" style="top:228px;">Oysters, warm champagne flambé</p>
  <div class="dots dots--grey" style="left:79px; top:252px; width:282px;"></div>

  <div class="course-head" style="top:264px;">
    <div class="flourish" role="img" aria-label="Small gold flourish ornament"></div>
    <div class="rule rule--top"></div>
    <svg class="course-heart course-heart--left" viewBox="0 0 24 22"><path d="M12 21s-10-6-10-13a5 5 0 0 1 10-2 5 5 0 0 1 10 2c0 7-10 13-10 13z" fill="#c9a24a"/></svg>
    <p class="course-name">DISH</p>
    <svg class="course-heart course-heart--right" viewBox="0 0 24 22"><path d="M12 21s-10-6-10-13a5 5 0 0 1 10-2 5 5 0 0 1 10 2c0 7-10 13-10 13z" fill="#c9a24a"/></svg>
    <div class="rule rule--bottom"></div>
  </div>
  <p class="course-desc" style="top:302px;">Grilled tournedos, braised endives and Jerusalem artichokes<br>Ranger Sauce Sole meunière, lemon sauce, steamed potatoes, rice</p>
  <div class="dots dots--grey" style="left:79px; top:336px; width:282px;"></div>

  <div class="course-head" style="top:347px;">
    <div class="flourish" role="img" aria-label="Small gold flourish ornament"></div>
    <div class="rule rule--top"></div>
    <svg class="course-heart course-heart--left" viewBox="0 0 24 22"><path d="M12 21s-10-6-10-13a5 5 0 0 1 10-2 5 5 0 0 1 10 2c0 7-10 13-10 13z" fill="#111"/></svg>
    <p class="course-name">DESSERT</p>
    <svg class="course-heart course-heart--right" viewBox="0 0 24 22"><path d="M12 21s-10-6-10-13a5 5 0 0 1 10-2 5 5 0 0 1 10 2c0 7-10 13-10 13z" fill="#111"/></svg>
    <div class="rule rule--bottom"></div>
  </div>
  <p class="course-desc" style="top:383px;">Tiramisu with red fruits - Flambéed Crêpe Suzette</p>

  <p class="price-label" style="top:400px; font-size:19px;">MENU AT</p>
  <div class="price-row" style="top:423px;">
    <svg width="26" height="24" viewBox="0 0 26 24"><polygon points="0,0 26,0 26,24 0,24 8,12" fill="#111"/></svg>
    <div class="price-box price-box--set">29.90€</div>
    <svg width="26" height="24" viewBox="0 0 26 24"><polygon points="0,0 26,0 18,12 26,24 0,24" fill="#111"/></svg>
  </div>

  <div class="contact">
    <div class="contact-item">
      <svg width="11" height="11" viewBox="0 0 24 24"><path d="M6.6 10.8a15 15 0 0 0 6.6 6.6l2.2-2.2a1 1 0 0 1 1-.25 11.4 11.4 0 0 0 3.6.57 1 1 0 0 1 1 1V20a1 1 0 0 1-1 1A17 17 0 0 1 3 4a1 1 0 0 1 1-1h3.5a1 1 0 0 1 1 1c0 1.250.2 2.450.57 3.570a1 1 0 0 1-.25 1z" fill="none" stroke="#111" stroke-width="2"/></svg>
      <span>Reservation required at:<br>06 38 72 15 09</span>
    </div>
    <div class="contact-divider"></div>
    <div class="contact-item">
      <svg width="11" height="12" viewBox="0 0 24 26"><path d="M12 2a7 7 0 0 0-7 7c0 5 7 12 7 12s7-7 7-12a7 7 0 0 0-7-7z" fill="none" stroke="#111" stroke-width="2"/><circle cx="12" cy="9" r="2.5" fill="none" stroke="#111" stroke-width="2"/><path d="M4 24h16" stroke="#111" stroke-width="2"/></svg>
      <span>18 rue Fernand<br>Gaudry 62870 VALMONT</span>
    </div>
  </div>
</section>

</body>
</html>
```